Mobile Spray tanner needs a Mobile Spray tanning business card design

I need a simple but eye-catching business card design. I would like the business card to be in two colours only (Hot pink background with black Silhouette & black writing). I would like the white behind the silhouette removed and the other bits on the silhouette removed (to be just a black silhouette with a hot pink bikini on). I would like the black writing to be aesthetically pleasing and quite artistic, but easy to read). Thank you very much

```html
<!DOCTYPE html>
<html lang="en">
<head>
<meta charset="utf-8">
<title>Golden Glow Mobile Spray Tanning – Business Card</title>
<link rel="stylesheet" href="https://fonts.googleapis.com/css2?family=Kalam:wght@400;700&display=swap">
<style>
  :root {
    --stage: #e9e4dc;
    --pink-edge: #ec6fb4;
    --pink-mid: #f29ccb;
    --pink-light: #f6b3d7;
    --ink: #111111;
    --rule: #ffffff;
  }
  html, body {
    margin: 0;
    width: 1200px;
    height: 848px;
    overflow: hidden;
    background: var(--stage);
  }
  .stage {
    position: relative;
    width: 1200px;
    height: 848px;
    display: flex;
    align-items: center;
    justify-content: center;
  }
  .business-card {
    position: relative;
    width: 1000px;
    height: 572px;
    background: radial-gradient(ellipse at 55% 60%, var(--pink-light) 0%, var(--pink-mid) 45%, var(--pink-edge) 100%);
    box-shadow: 0 10px 30px rgba(0, 0, 0, 0.25);
    overflow: hidden;
  }
  .edge-rules {
    position: absolute;
    inset: 0;
    width: 100%;
    height: 100%;
  }
  .figure-silhouette {
    position: absolute;
    left: 150px;
    top: 60px;
    width: 290px;
    height: 460px;
  }
  .card-text {
    position: absolute;
    left: 440px;
    top: 130px;
    width: 480px;
    margin: 0;
    font-family: "Kalam", cursive;
    font-weight: 700;
    color: var(--ink);
    text-align: center;
    text-transform: uppercase;
    letter-spacing: 2px;
    line-height: 1.22;
  }
  .card-text .line { display: block; }
  .card-text .name,
  .card-text .service-mobile { font-size: 46px; }
  .card-text .service { font-size: 50px; }
  .card-text .phone { font-size: 50px; margin-top: 8px; }
</style>
</head>
<body>
  <main class="stage">
    <section class="business-card">
      <svg class="edge-rules" viewBox="0 0 1000 572" aria-hidden="true">
        <path d="M34 0 Q18 286 34 572" fill="none" stroke="var(--rule)" stroke-width="3"/>
        <path d="M966 0 Q982 286 966 572" fill="none" stroke="var(--rule)" stroke-width="3"/>
      </svg>

      <svg class="figure-silhouette" viewBox="0 0 290 460" role="img"
           aria-label="Black silhouette of a kneeling woman wearing a hot pink bikini">
        <rect x="0" y="0" width="290" height="460" rx="40" fill="var(--ink)" opacity="0.85"/>
      </svg>

      <p class="card-text">
        <span class="line name">Golden Glow</span>
        <span class="line service-mobile">Mobile</span>
        <span class="line service">Spray Tranning</span>
        <span class="line phone">M. 0400 123 456</span>
      </p>
    </section>
  </main>
</body>
</html>
```